Bright Lantern Studios Business Card Design

Doug Farley

Managing Partner

Doug@BrightLanternStudios.com

BrightLanternStudios.com

502-417-2356

Industry/Entity Type

Photographer

Contact Information for Business Card

Doug Farley

Managing Partner

Doug@BrightLanternStudios.com

BrightLanternStudios.com

502-417-2356

Requirements
Must have
• Must show that I am a pavlo trusted photographer

```html
<!DOCTYPE html>
<html lang="en">
<head>
<meta charset="utf-8">
<title>Bright Lantern Studios Business Card</title>
<link rel="stylesheet" href="https://fonts.googleapis.com/css2?family=Josefin+Sans:wght@300;400;600&display=swap">
<style>
  :root {
    --backdrop: #dedede;
    --card-dark: #0b0b0b;
    --card-light: #f2f2f2;
    --ink-light: #ffffff;
    --ink-dark: #111111;
    --badge-green: #3a9a4a;
    --badge-gold: #f2b824;
    --badge-amber: #e89a1c;
  }
  html, body {
    margin: 0;
    padding: 0;
    width: 1200px;
    height: 960px;
    overflow: hidden;
    background: var(--backdrop);
  }
  .stage { display: block; width: 1200px; height: 960px; }
  .card-shadow { filter: drop-shadow(2px 3px 3px rgba(0,0,0,0.35)); }
  .type { font-family: "Josefin Sans", "Helvetica Neue", Arial, sans-serif; }
  .front-brand { fill: var(--ink-light); font-size: 22px; font-weight: 400; letter-spacing: 0.5px; }
  .front-tagline { fill: var(--ink-light); font-size: 13px; font-weight: 400; letter-spacing: 1.4px; }
  .front-name { fill: var(--ink-light); font-size: 20px; font-weight: 600; letter-spacing: 0.5px; }
  .front-title { fill: var(--ink-light); font-size: 15px; font-weight: 300; letter-spacing: 0.5px; }
  .front-phone { fill: var(--ink-light); font-size: 24px; font-weight: 400; letter-spacing: 1.5px; }
  .front-email { fill: var(--ink-light); font-size: 12px; font-weight: 400; letter-spacing: 1px; }
  .front-web { fill: var(--ink-light); font-size: 14px; font-weight: 400; letter-spacing: 1.2px; }
  .back-brand { fill: var(--ink-dark); font-size: 29px; font-weight: 400; letter-spacing: 0.5px; }
  .back-tagline { fill: var(--ink-dark); font-size: 14px; font-weight: 400; letter-spacing: 2.6px; }
  .rule-light { stroke: var(--ink-light); stroke-width: 1; }
  .rule-dark { stroke: var(--ink-dark); stroke-width: 1; }
</style>
</head>
<body>
<svg class="stage" viewBox="0 0 1200 960" xmlns="http://www.w3.org/2000/svg">
  <!-- Front card -->
  <g class="card-front">
    <path class="card-shadow" d="M438 95 H851 V437 H438 A171 171 0 0 1 438 95 Z" fill="var(--card-dark)" stroke="var(--card-light)" stroke-width="3"/>
    <circle class="brand-dot" cx="438" cy="266" r="88" fill="var(--card-light)"/>
    <g class="type">
      <text class="front-brand" x="816" y="146" text-anchor="end">BRIGHT LANTERN STUDIOS</text>
      <line class="rule-light" x1="562" y1="158" x2="816" y2="158"/>
      <text class="front-tagline" x="816" y="174" text-anchor="end">PAVLO TRUSTED PHOTOGRAPHER</text>
      <text class="front-name" x="816" y="278" text-anchor="end">DOUG FARLEY</text>
      <text class="front-title" x="816" y="298" text-anchor="end">MANAGING PARTNER</text>
      <text class="front-phone" x="816" y="340" text-anchor="end">502-417-2356</text>
      <text class="front-email" x="816" y="359" text-anchor="end">DOUG@BRIGHTLANTERNSTUDIOS.COM</text>
      <text class="front-web" x="816" y="391" text-anchor="end">BRIGHTLANTERNSTUDIOS.COM</text>
    </g>
  </g>

  <!-- Back card -->
  <g class="card-back">
    <path class="card-shadow" d="M375 482 H803 A172 172 0 0 1 803 826 H375 Z" fill="var(--card-light)"/>
    <circle class="brand-dot" cx="657" cy="598" r="40" fill="var(--ink-dark)"/>
    <g class="type">
      <text class="back-brand" x="659" y="690" text-anchor="middle">BRIGHT LANTERN STUDIOS</text>
      <line class="rule-dark" x1="494" y1="696" x2="824" y2="696"/>
      <text class="back-tagline" x="659" y="714" text-anchor="middle">PAVLO TRUSTED PHOTOGRAPHER</text>
    </g>
    <g class="trust-badge">
      <rect x="604" y="741" width="44" height="44" rx="3" fill="var(--badge-green)"/>
      <rect x="656" y="758" width="74" height="18" rx="2" fill="var(--badge-gold)"/>
      <rect x="664" y="776" width="58" height="6" rx="2" fill="var(--badge-amber)"/>
    </g>
  </g>
</svg>
</body>
</html>
```